Automotive eCommerce Business looking for a business card design

Looking for a clean and simple business card design. Our company name is "Harbor Crest Auto" and we are a company specializing in the ecommerce sales of automotive parts, specifically for pick up trucks and large SUVs. Our company colours are red, black, and white.

Feel free to use the logo provided or create a new logo that you seem fit. Looking forward to your creative ideas!

Industry/Entity Type

Automotive

Contact Information for Business Card

We were thinking of a possibly two-sided design featuring just the logo and company name on one side, and personal information on the other side. Single sided designs will be considered as well.

Font styles to use
Serif
Sans Serif
Decorative

Colors
ec1f27
ffffff
000000

Requirements
Must have
• Space for employee's name, title, phone number and email address, along with the company address and website somewhere.

```html
<!DOCTYPE html>
<html lang="en">
<head>
<meta charset="utf-8">
<title>Harbor Crest Auto – Business Card</title>
<link rel="stylesheet" href="https://fonts.googleapis.com/css2?family=Arimo:wght@400;700&display=swap">
<style>
  :root {
    --stage: #2a2a2a;
    --brand-red: #a81c24;
    --brand-red-deep: #8e1820;
    --accent-pink: #c98f93;
    --paper: #ffffff;
    --paper-shade: #f0f0f0;
    --ink: #1a1a1a;
    --ink-soft: #333333;
  }
  * { box-sizing: border-box; margin: 0; padding: 0; }
  html, body {
    width: 1200px; height: 997px; overflow: hidden;
    background: var(--stage);
    font-family: "Arimo", Arial, sans-serif;
  }
  .canvas {
    position: relative; width: 1200px; height: 997px;
  }
  .card {
    position: absolute; left: 260px; width: 680px; height: 389px;
    box-shadow: 0 12px 30px rgba(0,0,0,.45);
    overflow: hidden;
  }
  /* Back side */
  .card-back {
    top: 70px;
    background: linear-gradient(135deg, #b21f28, var(--brand-red-deep));
    display: flex; align-items: center; justify-content: center;
  }
  .brand-back {
    display: flex; align-items: center; gap: 16px;
    color: var(--paper); font-weight: 700; font-size: 44px; letter-spacing: .5px;
  }
  .brand-back .brand-mark {
    width: 40px; height: 40px; background: var(--paper);
  }
  /* Front side */
  .card-front {
    top: 530px;
    background: linear-gradient(180deg, var(--paper), var(--paper-shade));
  }
  .decor-block {
    position: absolute; left: 370px; right: 0; top: 0; bottom: 0;
    background: var(--accent-pink); opacity: .75;
  }
  .brand-front {
    position: absolute; left: 36px; top: 54px;
    display: flex; align-items: center; gap: 10px;
    color: var(--brand-red); font-weight: 700; font-size: 26px;
    white-space: nowrap;
  }
  .brand-front .brand-mark {
    width: 26px; height: 26px; background: var(--brand-red);
  }
  .person {
    position: absolute; left: 40px; top: 150px;
  }
  .person-name {
    color: var(--brand-red); font-weight: 700; font-size: 19px; letter-spacing: .5px;
  }
  .person-title {
    color: var(--ink); font-size: 14px; margin-top: 2px;
  }
  .address {
    position: absolute; left: 40px; top: 208px;
    color: var(--ink-soft); font-size: 12.5px; line-height: 1.45;
  }
  .contact-list {
    position: absolute; left: 40px; top: 258px; list-style: none;
  }
  .contact-list li {
    display: flex; align-items: center; gap: 10px;
    color: var(--ink); font-size: 18px; line-height: 1.45;
  }
  .contact-icon {
    width: 17px; height: 17px; flex: none;
  }
  .website {
    position: absolute; left: 40px; top: 346px;
    color: var(--brand-red); font-weight: 700; font-size: 15px; letter-spacing: 1px;
  }
</style>
</head>
<body>
<main class="canvas">

  <section class="card card-back" aria-label="Card back">
    <div class="brand-back">
      <span class="brand-mark"></span>
      <span class="brand-name">Harbor Crest Auto</span>
    </div>
  </section>

  <section class="card card-front" aria-label="Card front">
    <div class="decor-block"></div>

    <div class="brand-front">
      <span class="brand-mark"></span>
      <span class="brand-name">Harbor Crest Auto</span>
    </div>

    <div class="person">
      <p class="person-name">LAURA BENNETT</p>
      <p class="person-title">Owner</p>
    </div>

    <p class="address">418 Bayshore Ave, Suite 210<br>Port Lavaca, Texas 77979</p>

    <ul class="contact-list">
      <li>
        <svg class="contact-icon" viewBox="0 0 20 20" aria-hidden="true">
          <circle cx="10" cy="10" r="10" fill="var(--brand-red)"/>
          <path d="M6.5 5.5c.6-.5 1.3-.4 1.6.2l.8 1.5c.2.5.1 1-.3 1.3l-.5.4c.6 1.2 1.5 2.1 2.7 2.7l.4-.5c.3-.4.8-.5 1.3-.3l1.5.8c.6.3.7 1 .2 1.6l-.7.7c-.6.6-1.5.7-2.3.3-2.4-1.1-4.200-2.9-5.3-5.3-.4-.8-.3-1.7.3-2.3z" fill="#fff"/>
        </svg>
        0455 302 718
      </li>
      <li>
        <svg class="contact-icon" viewBox="0 0 20 20" aria-hidden="true">
          <circle cx="10" cy="10" r="10" fill="var(--brand-red)"/>
          <rect x="5" y="8" width="10" height="6" rx="1" fill="#fff"/>
          <path d="M5 8.5c1-2.5 9-2.5 10 0" stroke="#fff" stroke-width="1.6" fill="none"/>
        </svg>
        1300 417 925
      </li>
      <li>
        <svg class="contact-icon" viewBox="0 0 20 20" aria-hidden="true">
          <circle cx="10" cy="10" r="10" fill="var(--brand-red)"/>
          <rect x="5" y="6.5" width="10" height="7" fill="#fff"/>
          <path d="M5 6.5l5 4 5-4" stroke="var(--brand-red)" stroke-width="1" fill="none"/>
        </svg>
        lbennett@hcauto.com
      </li>
    </ul>

    <p class="website">WWW.HARBORCRESTAUTO.COM</p>
  </section>

</main>
</body>
</html>
```